Gardowell - Direct Mail DL flyer design

Create a direct market flyer (d/l size) to compel people to act and visit our website to buy life insurance.

Copy, example images and notes are provided

Target Market(s)

Families with debt who need life insurance

Industry/Entity Type

Insurance

Requirements
Must have
• Our logo
• Colours are Blue C99, M79, Y0, K0 Green C40, M0, Y100, K0
• Copy side 1 is "For the price of a coffee you can ensure you and your family get the right start."
• Copy side 2 is "It doesn't sound like much, but when it comes to life insurance, $1 a day* can make a huge difference if you were to die.
• For the cost of a cup of coffee a day, you can ensure your family will be left with enough to protect the home, pay for ongoing living expenses and fund your children's continued education.
• Your life is important
• Apply today and get 1 month free cover
• Build your tomorrow
• company logo gardowell.com.au make prominant
• *For a monthly premium of $25.33, a 35 year old non-smoking male can obtain $300,000 of term life cover.
• Example for illistration purpose only. The premium cited is current as at February 2016, is based on the factors referred to in the example and subject to underwriting. You should consider whether this product is appropriate for you. Refer to the Product Disclosure Statement, available from gardowell before deciding whether to acquire the product."
• Footer
• Gardowell Pty Ltd
• ABN 47 253 918 604 AFS Licence 729140
Nice to have
• Coffee cup with pods/capsuals around it white background side 1 and coffee ring stain on reverse as watermark
• Trusafe has been awarded - Merrow Ratings - 2014 Kestrel Protection Honours for Term Cover
• Trusafe has been awarded - Merrow Ratings - 2015 Kestrel Protection Honours for Term Cover

```html
<!DOCTYPE html>
<html lang="en">
<head>
<meta charset="utf-8">
<title>Gardowell DL Flyer</title>
<link rel="stylesheet" href="https://fonts.googleapis.com/css2?family=Roboto+Condensed:ital,wght@0,400;0,700;1,700&family=Lato:ital,wght@0,400;0,700;1,400;1,700&family=Merriweather+Sans:wght@700&family=Arimo:wght@700&display=swap">
<style>
:root{
  --brand-blue:#1f44b4;
  --brand-blue-light:#3766d6;
  --brand-green:#8dc63f;
  --brand-green-bright:#9fdc2e;
  --ink:#1d2430;
  --muted:#5a6270;
  --paper:#ffffff;
  --stage:#e6e8eb;
  --band-grey:#e9eaec;
  --footer-black:#1a1a1a;
}
*{box-sizing:border-box;margin:0;padding:0}
html,body{width:1200px;height:902px;overflow:hidden;background:var(--stage)}
.canvas{position:relative;width:1200px;height:902px}
.flyer{position:absolute;top:36px;width:400px;height:830px;background:var(--paper);overflow:hidden;box-shadow:0 2px 10px rgba(0,0,0,.18)}
.flyer--front{left:150px}
.flyer--back{left:650px}
.abs{position:absolute}

/* brand */
.brand{position:absolute;display:flex;align-items:center;gap:10px}
.brand__mark{width:44px;height:44px;background:var(--brand-green);border-radius:6px}
.brand__name{font-family:"Lato",sans-serif;font-weight:700;font-size:29px;color:var(--brand-blue);line-height:1}
.brand__tagline{position:absolute;left:109px;top:68px;font-family:"Lato",sans-serif;font-size:12px;letter-spacing:2.2px;color:var(--brand-blue)}

/* front */
.front__photo{left:0;top:290px;width:400px;height:400px;background:
  radial-gradient(ellipse 60% 55% at 60% 62%,rgba(240,226,200,.55) 0%,rgba(240,226,200,0) 70%),
  linear-gradient(160deg,#b98a47 0%,#a0703a 45%,#7a4f24 100%)}
.front__band{left:0;top:78px;width:400px;height:250px}
.front__headline{left:0;top:138px;width:400px;text-align:center;font-family:"Roboto Condensed",sans-serif;color:var(--paper)}
.front__headline .line-caps{font-weight:400;font-size:28px;line-height:34px}
.front__headline .line-accent{font-weight:700;font-style:italic;font-size:28px;line-height:34px;color:var(--brand-green-bright)}
.front__headline .line-start{font-family:"Arimo",sans-serif;font-weight:700;font-size:23px;line-height:40px;margin-top:2px}
.front__footer{left:0;top:660px;width:400px;height:140px}
.contact-pill{left:128px;top:666px;width:142px;height:28px;border-radius:8px 8px 0 0;background:var(--brand-blue);color:var(--paper);font-family:"Lato",sans-serif;font-weight:700;font-size:15px;text-align:center;line-height:28px}
.front__company{left:0;top:718px;width:400px;text-align:center;font-family:"Lato",sans-serif;font-weight:700;font-size:14px;line-height:19px;color:var(--ink)}
.follow{left:0;top:764px;width:400px;display:flex;justify-content:center;align-items:center;gap:6px;font-family:"Lato",sans-serif;font-weight:700;font-size:11px;color:var(--ink)}
.follow__dot{width:14px;height:14px;border-radius:50%;background:var(--ink)}
.front__web{left:0;top:790px;width:400px;height:40px;background:var(--footer-black);color:var(--brand-green-bright);font-family:"Lato",sans-serif;font-weight:700;font-size:13px;letter-spacing:2.6px;text-align:center;line-height:40px}

/* back */
.back__head{left:0;top:22px;width:400px;text-align:center;font-family:"Roboto Condensed",sans-serif}
.back__head .h-blue{font-weight:400;font-size:29px;line-height:34px;color:var(--brand-blue)}
.back__head .h-italic{font-weight:700;font-style:italic;font-size:21px;line-height:30px;color:var(--brand-green)}
.back__head .h-price{font-weight:400;font-size:27px;line-height:36px;color:var(--brand-blue)}
.back__head .h-green{font-family:"Arimo",sans-serif;font-weight:700;font-size:17px;line-height:22px;color:var(--brand-green)}
.back__arc{left:0;top:196px;width:400px;height:70px}
.back__photo{left:0;top:240px;width:400px;height:214px;background:
  radial-gradient(ellipse 70% 80% at 50% 70%,rgba(226,196,170,.35) 0%,rgba(226,196,170,0) 70%),
  linear-gradient(180deg,#f6f6f5 0%,#e4e3e0 70%,#d3d5d8 100%)}
.back__title{left:0;top:456px;width:400px;height:54px;background:linear-gradient(#f6f6f7,var(--band-grey));border-bottom:2px solid var(--brand-blue);text-align:center;font-family:"Merriweather Sans",sans-serif;font-weight:700;font-size:28px;line-height:52px;color:var(--ink)}
.back__body{left:0;top:510px;width:400px;height:112px;background:linear-gradient(var(--brand-blue-light),var(--brand-blue));color:var(--paper);font-family:"Lato",sans-serif;font-size:13.5px;line-height:20px;text-align:center;padding:18px 28px 0}
.coupon{left:0;top:622px;width:400px;height:132px;background:var(--paper);border-top:2px dashed var(--brand-blue);border-bottom:2px dashed var(--brand-blue);padding:8px 18px 0 30px}
.coupon__offer{font-family:"Roboto Condensed",sans-serif;font-size:20px;color:var(--brand-blue);line-height:26px}
.coupon__offer b{color:var(--brand-green);font-weight:700}
.coupon__note{margin-top:4px;font-family:"Lato",sans-serif;font-style:italic;font-weight:700;font-size:11.5px;line-height:15px;color:var(--ink)}
.coupon__note .star{color:var(--brand-blue);font-size:14px}
.coupon__legal{margin-top:4px;font-family:"Lato",sans-serif;font-style:italic;font-size:7px;line-height:9px;color:var(--muted)}
.back__band{left:0;top:758px;width:400px;height:36px}
.back__footmark{left:80px;top:794px;width:32px;height:32px;background:var(--brand-green);border-radius:5px}
.back__company{right:44px;top:797px;text-align:right;font-family:"Lato",sans-serif;font-weight:700;font-size:11px;line-height:15px;color:var(--ink)}
</style>
</head>
<body>
<main class="canvas">

  <section class="flyer flyer--front" aria-label="Flyer side one">
    <div class="brand" style="left:55px;top:22px">
      <span class="brand__mark" aria-hidden="true"></span>
      <span class="brand__name">gardowell.com.au</span>
    </div>
    <p class="brand__tagline">build your tomorrow</p>

    <div class="abs front__photo" role="img" aria-label="Photo of a woman with closed eyes savouring a steaming white cup of coffee in warm light"></div>

    <svg class="abs front__band" viewBox="0 0 400 250" aria-hidden="true">
      <defs>
        <radialGradient id="bandGlow" cx="50%" cy="40%" r="70%">
          <stop offset="0" stop-color="#3f72e0"/>
          <stop offset="1" stop-color="#1a3aa6"/>
        </radialGradient>
      </defs>
      <path d="M0 40 Q200 -10 400 40 L400 210 Q200 270 0 210 Z" fill="var(--brand-green)"/>
      <path d="M0 48 Q200 2 400 48 L400 204 Q200 262 0 204 Z" fill="url(#bandGlow)"/>
      <path d="M0 204 Q200 262 400 204 L400 214 Q200 272 0 214 Z" fill="#5b7ff0"/>
    </svg>

    <div class="abs front__headline">
      <p class="line-caps">FOR THE PRICE OF A COFFEE</p>
      <p class="line-accent">You can ensure you</p>
      <p class="line-accent">and your family</p>
      <p class="line-start">GET THE RIGHT START</p>
    </div>

    <svg class="abs front__footer" viewBox="0 0 400 140" aria-hidden="true">
      <path d="M0 30 Q200 -10 400 30 L400 140 L0 140 Z" fill="var(--brand-blue)"/>
      <path d="M0 36 Q200 -2 400 36 L400 140 L0 140 Z" fill="var(--paper)"/>
      <path d="M0 42 Q200 6 400 42 L400 140 L0 140 Z" fill="var(--brand-green-bright)"/>
    </svg>
    <div class="abs contact-pill">Contact Us</div>
    <div class="abs front__company">
      <p>Gardowell Pty Ltd</p>
      <p>ABN 47 253 918 604 AFS Licence 729140</p>
    </div>
    <div class="abs follow"><span>Follow Us on</span><span class="follow__dot"></span><span class="follow__dot"></span></div>
    <div class="abs front__web">www.gardowell.com.au</div>
  </section>

  <section class="flyer flyer--back" aria-label="Flyer side two">
    <div class="abs back__head">
      <p class="h-blue">IT DOESN'T SOUND LIKE MUCH,</p>
      <p class="h-italic">But when it comes to life insurance,</p>
      <p class="h-price">$1 A DAY *</p>
      <p class="h-green">CAN MAKE A HUGE DIFFERENCE</p>
      <p class="h-green">IF YOU WERE TO DIE</p>
    </div>

    <div class="abs back__photo" role="img" aria-label="Photo of a smiling family of four, mother, father and two young children hugging"></div>

    <svg class="abs back__arc" viewBox="0 0 400 70" aria-hidden="true">
      <path d="M0 40 Q180 -8 400 26 L400 70 L0 70 Z" fill="var(--brand-blue)"/>
      <path d="M0 48 Q180 4 400 36 L400 70 L0 70 Z" fill="var(--brand-green)"/>
      <path d="M0 54 Q180 12 400 44 L400 70 L0 70 Z" fill="#f4f4f3"/>
    </svg>

    <h2 class="abs back__title">Your life is important</h2>
    <p class="abs back__body">For the cost of a cup of coffee a day, you can ensure your family will be left with enough to protect the home, pay for ongoing living expenses and fund your children's continued education.</p>

    <div class="abs coupon">
      <p class="coupon__offer">Apply today and get <b>1 MONTH FREE</b> cover</p>
      <p class="coupon__note"><span class="star">*</span> For a monthly premium of $25.33,<br>&nbsp;&nbsp;A 35 year old non-smoking male can obtain $300,000<br>&nbsp;&nbsp;of term life cover.</p>
      <p class="coupon__legal">Example for illustration purpose only. The premium cited is current as at February 2016, is based on the factors referred to in the example and subject to underwriting. You should consider whether this product is appropriate for you. Refer to the Product Disclosure Statement, available from gardowell before deciding whether to acquire the product.</p>
    </div>

    <svg class="abs back__band" viewBox="0 0 400 36" aria-hidden="true">
      <rect width="400" height="36" fill="var(--brand-blue)"/>
      <path d="M0 36 Q200 6 400 22 L400 36 Z" fill="var(--brand-green)"/>
      <path d="M0 36 Q200 12 400 28 L400 36 Z" fill="var(--paper)"/>
    </svg>
    <span class="abs back__footmark" aria-hidden="true"></span>
    <div class="abs back__company">
      <p>Gardowell Pty Ltd</p>
      <p>ABN 47 253 918 604 AFS Licence 729140</p>
    </div>
  </section>

</main>
</body>
</html>
```